Halden & Pruitt Periodontics and Implant Solutions Business Card

We are a specialty dental practice- implants and periodontal surgery. We have just re-designed our logo and are building a new office and would like to re-design our business card. We are looking for something professional with a creative and artsy twist- something to stand out among the rest! Happy Designing!

I have uploaded all versions of our new logo and our current business card. We have 3 locations and 2 doctors.

Target Market(s)

55+

Industry/Entity Type

Dental

Contact Information for Business Card

Needs Names, logo, locations- professional and artsy!

Colors
0555a3
0592cd
34a7d7
3277b5
85cae6
85acd3
cee9f5
ecf7fb

Requirements
Must have
• our names:
• Thomas E. Halden D.M.D.
• Celia M. Pruitt D.M.D.
• Diplomate of the National Council of Gum Surgery
• Address locations:
• 462 W. Larkspur Avenue Suite 210B Plantation, FL 33871
• Tel: 954-318-2264 Fax: 954-318-2291
• 5127 Harlow Lane #C-4 Boca Raton, FL 33609
• Tel: 561-627-1958 Fax: 561-703-2816
• 274 Northwest 9th Street #412 Miami FL 33987
• Tel: 786-429-6153 Fax: 786-429-6170
Nice to have
• unique look
Should not have
• doesn't need QR like our current card has.

```html
<!DOCTYPE html>
<html lang="en">
<head>
<meta charset="utf-8">
<title>Halden &amp; Pruitt Business Card</title>
<link rel="stylesheet" href="https://fonts.googleapis.com/css2?family=Questrial&family=Roboto:wght@400;500&display=swap">
<style>
  :root {
    --navy: #2b3480;
    --grey: #7a7a7c;
    --text-grey: #6b6b6e;
    --card: #ffffff;
    --stage: #e8e8ea;
  }
  * { margin: 0; padding: 0; box-sizing: border-box; }
  html, body { width: 1200px; height: 726px; overflow: hidden; background: var(--stage); }
  .canvas { position: relative; width: 1200px; height: 726px; }
  .card {
    position: absolute; width: 540px; height: 308px; background: var(--card);
    overflow: hidden; box-shadow: 0 2px 6px rgba(0,0,0,.12);
  }
  .card--front { left: 40px; top: 209px; }
  .card--back { left: 620px; top: 209px; }
  .card__swoosh { position: absolute; inset: 0; }

  .brand { position: absolute; display: flex; align-items: center; gap: 10px; }
  .brand__mark { width: 64px; height: 64px; border-radius: 50%; border: 5px solid var(--navy); flex: none; }
  .brand__name {
    font-family: "Questrial", sans-serif; color: var(--navy); line-height: 1.05;
    font-size: 26px; letter-spacing: .5px; white-space: nowrap;
  }
  .brand__name small { display: block; font-size: 13px; letter-spacing: .2px; margin-top: 2px; }
  .card--front .brand { left: 28px; top: 24px; }
  .card--back .brand { left: 140px; top: 44px; }

  .doctors {
    position: absolute; right: 28px; top: 96px; text-align: right;
    font-family: "Questrial", sans-serif; color: var(--navy); white-space: nowrap;
  }
  .doctors__name { font-size: 19px; line-height: 1.2; }
  .doctors__title { font-size: 11px; color: var(--text-grey); margin-top: 5px; letter-spacing: .2px; }

  .contact {
    position: absolute; left: 36px; top: 244px; list-style: none;
    font-family: "Roboto", sans-serif; font-size: 12.5px; color: #fff;
  }
  .contact li { display: flex; align-items: center; gap: 10px; height: 17px; }
  .contact svg { width: 12px; height: 12px; flex: none; }

  .locations {
    position: absolute; left: 0; right: 0; top: 140px; text-align: center;
    font-family: "Roboto", sans-serif; font-size: 12px; color: var(--text-grey); line-height: 1.4;
  }
  .location + .location { margin-top: 12px; }
  .location__label { color: var(--navy); }
  .card__band { position: absolute; left: 0; right: 0; bottom: 0; height: 26px; background: var(--navy); }
</style>
</head>
<body>
<main class="canvas">

  <section class="card card--front" aria-label="Business card front">
    <svg class="card__swoosh" viewBox="0 0 540 308" preserveAspectRatio="none" aria-hidden="true">
      <path d="M0,218 C190,208 370,196 540,168 L540,180 C370,210 190,222 0,228 Z" fill="var(--grey)"/>
      <path d="M0,234 C190,226 370,214 540,188 L540,308 L0,308 Z" fill="var(--navy)"/>
    </svg>

    <div class="brand">
      <span class="brand__mark"></span>
      <p class="brand__name">HALDEN &amp; PRUITT<small>Periodontics and Implant Solutions</small></p>
    </div>

    <div class="doctors">
      <p class="doctors__name">Thomas E. Halden, D.M.D.</p>
      <p class="doctors__name">Celia M. Pruitt, D.M.D.</p>
      <p class="doctors__title">Diplomate of the National Council of Gum Surgery</p>
    </div>

    <ul class="contact">
      <li>
        <svg viewBox="0 0 12 12" aria-hidden="true"><path d="M2 1h2.5l1 3-1.5 1a6 6 0 0 0 3 3l1-1.5 3 1V10a1 1 0 0 1-1 1A9 9 0 0 1 1 2a1 1 0 0 1 1-1z" fill="#fff"/></svg>
        954-318-2264
      </li>
      <li>
        <svg viewBox="0 0 12 12" aria-hidden="true"><g fill="none" stroke="#fff" stroke-width="1"><circle cx="6" cy="6" r="5"/><ellipse cx="6" cy="6" rx="2.2" ry="5"/><path d="M1 6h10"/></g></svg>
        www.haldenpruittperio.com
      </li>
      <li>
        <svg viewBox="0 0 12 12" aria-hidden="true"><g fill="none" stroke="#fff" stroke-width="1"><rect x="1" y="2.5" width="10" height="7"/><path d="M1 2.5l5 4 5-4"/></g></svg>
        hello@haldenpruittperio.com
      </li>
    </ul>
  </section>

  <section class="card card--back" aria-label="Business card back">
    <div class="brand">
      <span class="brand__mark"></span>
      <p class="brand__name">HALDEN &amp; PRUITT<small>Periodontics and Implant Solutions</small></p>
    </div>

    <div class="locations">
      <div class="location">
        <p>462 W. Larkspur Avenue Suite 210B Plantation, FL 33871</p>
        <p><span class="location__label">Tel:</span> 954-318-2264 <span class="location__label">| Fax:</span> 954-318-2291</p>
      </div>
      <div class="location">
        <p>274 Northwest 9th Street #412 Miami, FL 33987</p>
        <p><span class="location__label">Tel:</span> 786-429-6153 <span class="location__label">| Fax:</span> 786-429-6170</p>
      </div>
      <div class="location">
        <p>5127 Harlow Lane #C-4 Boca Raton, FL 33609</p>
        <p><span class="location__label">Tel:</span> 561-627-1958 <span class="location__label">| Fax:</span> 561-703-2816</p>
      </div>
    </div>

    <div class="card__band"></div>
  </section>

</main>
</body>
</html>
```